TK AG Flyer design

I’d like to redesign an A5, double-sided flyer for the company TK AG (www.tkag.lu). The text/content is available in a Word document.

```html
<!DOCTYPE html>
<html lang="de">
<head>
<meta charset="utf-8">
<title>TK AG – Flyer</title>
<link href="https://fonts.googleapis.com/css2?family=Poppins:wght@400;500;600;700;800&family=Oswald:wght@600&display=swap" rel="stylesheet">
<style>
  :root{
    --navy:#0b0a85;
    --navy-deep:#07076e;
    --orange:#f7a04a;
    --orange-text:#f59a3a;
    --ink:#2b2b2b;
    --band:#e6e7e9;
    --page:#f1f1f1;
    --white:#ffffff;
  }
  *{box-sizing:border-box;margin:0;padding:0}
  html,body{width:1024px;height:1200px;overflow:hidden;background:var(--page)}
  body{font-family:"Poppins",sans-serif;color:var(--ink);position:relative}
  .flyer{
    position:absolute;left:111px;top:30px;width:1022px;height:1452px;
    background:var(--white);transform:scale(0.785);transform-origin:0 0;overflow:hidden;
  }
  .abs{position:absolute}

  /* header */
  .brand{left:0;right:0;top:112px;display:flex;justify-content:center;align-items:center;gap:18px}
  .brand-square{width:40px;height:40px;background:var(--orange)}
  .brand-name{font-size:44px;font-weight:500;color:var(--ink);letter-spacing:1px;line-height:1}

  /* hero */
  .hero{left:0;top:225px;width:1022px;height:515px;overflow:hidden}
  .hero svg{position:absolute;inset:0}
  .hero-shade{position:absolute;inset:0;background:linear-gradient(180deg,rgba(11,10,133,0) 38%,rgba(11,10,133,.75) 68%,var(--navy-deep) 92%)}
  .headline{left:0;right:0;top:478px;text-align:center;color:var(--white);font-weight:800;font-size:70px;line-height:66px;letter-spacing:-1.5px}
  .headline-sub{left:0;right:0;top:606px;text-align:center;color:var(--white);font-size:29px;font-weight:400;letter-spacing:1px}
  .divider{left:339px;top:656px;width:342px;height:8px}
  .claims{left:0;right:0;top:684px;text-align:center;color:var(--orange-text);font-size:17.5px;letter-spacing:.3px}
  .claims span.sep{margin:0 14px}

  /* body */
  .intro{left:82px;top:773px;font-size:16.5px}
  .tag{left:82px;height:44px;padding:0 50px 0 24px;display:flex;align-items:center;color:var(--white);font-size:21px;font-weight:400;letter-spacing:.5px;
       clip-path:polygon(0 0,100% 0,calc(100% - 24px) 100%,0 100%)}
  .tag b{font-weight:700;margin-right:6px}
  .tag--solar{top:822px;background:var(--navy)}
  .tag--efficiency{top:1025px;background:var(--orange)}
  .lead{left:82px;font-size:17px;font-weight:600}
  .list{left:98px;list-style:none;font-size:17px;line-height:25.5px}
  .list li{position:relative;padding-left:15px}
  .list li::before{content:"";position:absolute;left:-3px;top:10px;width:6px;height:6px;border-radius:50%;background:var(--white);border:1.5px solid #555}
  .list::before{content:"";position:absolute;left:0;top:13px;bottom:13px;width:1px;background:#777}
  .list b{font-weight:600}

  .cta{left:716px;top:1037px;width:240px;height:240px;border-radius:50%;
       background:radial-gradient(circle at 50% 30%,#1d1aa8,var(--navy) 70%);color:var(--white);text-align:center;padding-top:42px}
  .cta-title{font-size:24px;font-weight:700;line-height:23px}
  .cta-note{margin-top:14px;font-size:10px;font-weight:700;color:var(--orange-text);line-height:13px}

  /* partner band */
  .band{left:0;top:1240px;width:1022px;height:65px;background:var(--band)}
  .group{left:88px;top:1256px;font-size:13px;line-height:20px;color:#333}
  .group strong{font-weight:500}
  .partners{left:648px;top:1255px;display:flex;gap:24px}
  .badge{height:22px;border-radius:3px;background:#b9babd}
  .legal{right:81px;top:1282px;font-size:11.5px;color:#555}

  /* footer */
  .footer{left:0;top:1305px;width:1022px;height:147px;background:var(--navy-deep)}
  .phone{left:88px;top:1345px;display:flex;align-items:center;gap:12px;color:var(--white);font-family:"Oswald",sans-serif;font-weight:600;font-size:48px;line-height:1}
  .address{right:86px;top:1355px;text-align:right;color:var(--white);font-size:17px;line-height:25px}
</style>
</head>
<body>
<main class="flyer">
  <header class="abs brand">
    <span class="brand-square"></span>
    <span class="brand-name">TK AG</span>
  </header>

  <section class="abs hero">
    <svg width="1022" height="515" viewBox="0 0 1022 515">
      <defs>
        <linearGradient id="photoTone" x1="0" y1="0" x2="0" y2="1">
          <stop offset="0" stop-color="#8fb6e0"/>
          <stop offset=".3" stop-color="#b9cfe2"/>
          <stop offset=".45" stop-color="#3d4f88"/>
          <stop offset="1" stop-color="#14206a"/>
        </linearGradient>
        <linearGradient id="studioTone" x1="0" y1="0" x2="0" y2="1">
          <stop offset="0" stop-color="#c3c3c3"/>
          <stop offset="1" stop-color="#a9a9b8"/>
        </linearGradient>
      </defs>
      <rect width="1022" height="515" fill="url(#studioTone)" role="img" aria-label="Schnittmodell eines Hauses mit Solaranlage, Heizung und Haustechnik"/>
      <polygon points="0,0 591,0 300,515 0,515" fill="url(#photoTone)" role="img" aria-label="Foto: Dach mit Indach-Solarmodulen vor Hügellandschaft"/>
    </svg>
    <div class="hero-shade"></div>
  </section>

  <h1 class="abs headline">SOLAR ENERGIE &amp;<br>ENERGIE EFFIZIENZ</h1>
  <p class="abs headline-sub">AUS EINER HAND</p>
  <svg class="abs divider" viewBox="0 0 342 8"><line x1="4" y1="4" x2="338" y2="4" stroke="#fff" stroke-width="2"/><circle cx="4" cy="4" r="4" fill="#fff"/><circle cx="338" cy="4" r="4" fill="#fff"/></svg>
  <p class="abs claims">MEHR EIGENVERBRAUCH<span class="sep">•</span>MEHR EFFIZIENZ<span class="sep">•</span>MEHR ZUKUNFT</p>

  <p class="abs intro">Wir planen und beraten rund um Photovoltaik und Energieeffizienz – für Private, Gewerbe und Industrie.</p>

  <h2 class="abs tag tag--solar"><b>SOLAR</b> ENERGIE</h2>
  <p class="abs lead" style="top:883px">Photovoltaik-Lösungen, die zu Ihrem Dach passen</p>
  <ul class="abs list" style="top:917px">
    <li><b>Indach PV-Anlagen</b> (integriert &amp; ästhetisch)</li>
    <li><b>Aufdach PV-Anlagen</b> (effizient &amp; preis-/leistungsstark)</li>
    <li><b>Eigenverbrauch optimieren</b> (Batterie, Wärmepumpe, E-Mobility, smartes Lastmanagement)</li>
  </ul>

  <h2 class="abs tag tag--efficiency"><b>ENERGIE</b> EFFIZIENZ</h2>
  <p class="abs lead" style="top:1088px">Beratung &amp; Konzepte für nachhaltige Gebäude</p>
  <ul class="abs list" style="top:1122px">
    <li><b>Energieberatung / GEA / GEA Plus</b></li>
    <li><b>Impulsberatung &amp; Energiekonzept</b> (HLK + PV, Simulationen, Nachweise)</li>
    <li><b>Energiesanierung</b> (Planung, Koordination, Förderabwicklung)</li>
  </ul>

  <aside class="abs cta">
    <p class="cta-title">Jetzt<br>unverbindlich<br>Kontakt<br>aufnehmen</p>
    <p class="cta-note">TELEFON ODER E-MAIL – WIR<br>MELDEN UNS ZEITNAH.</p>
  </aside>

  <div class="abs band"></div>
  <p class="abs group"><strong>Mitglied der Firmengruppe</strong><br>Nordwerk Luzern AG - Netzwerk I Kompetenz I Innovation</p>
  <div class="abs partners">
    <span class="badge" style="width:136px"></span>
    <span class="badge" style="width:128px"></span>
  </div>
  <p class="abs legal">Datenschutz &nbsp;|&nbsp; Impressum</p>

  <footer class="abs footer"></footer>
  <p class="abs phone">
    <svg width="28" height="48" viewBox="0 0 28 48"><rect x="2" y="2" width="24" height="44" rx="4" fill="none" stroke="#f7a04a" stroke-width="3"/><line x1="10" y1="40" x2="18" y2="40" stroke="#f7a04a" stroke-width="2.5"/></svg>
    +41 41 555 0142
  </p>
  <p class="abs address">Seeblickweg 12, CH-6015 Luzern<br>www.tkag.lu &nbsp;|&nbsp;&nbsp; info@tkag.lu</p>
</main>
</body>
</html>
```